Online Course Page

We are building a video based online course page. This project is for only the actual page that the student will watch the videos at. They will watch one vide at a time. Once one video lesson is completed then they can move to the next video lesson. The page will need to show the video player. (Main feature.) The list of lessons in the course. Instructor information. Profile picture and bio of the instructor. A Live chat button that will initiate a chat in real-time with the instructor.

The winning designer will also be asked to to design the dashboard area and other aspects of the user interface as an additional project.

Target Market(s)

Adults

Number of Pages Required

1 page

Colors
9bcb3c

Requirements
Must have
• Our logo is attached. Green and grey are our colors. Should feel modern, clean and be simple to navigate. The site will be responsive so the layout should work well on mobile devices.

```html
<!DOCTYPE html>
<html lang="en">
<head>
<meta charset="utf-8">
<title>Course Lesson</title>
<link href="https://fonts.googleapis.com/css2?family=Lato:wght@400;700&display=swap" rel="stylesheet">
<style>
:root{
  --green:#9bcb3c;
  --black:#111111;
  --ink:#222222;
  --text:#4a4a4a;
  --muted:#8a8a8a;
  --line:#e3e3e3;
  --page:#f7f8fa;
  --white:#ffffff;
}
*{box-sizing:border-box;margin:0;padding:0}
html,body{width:1200px;height:775px;overflow:hidden}
body{font-family:'Lato',sans-serif;background:var(--page);color:var(--ink);position:relative}
.topbar{position:absolute;left:0;top:0;width:1200px;height:37px;background:var(--black);color:#fff;font-size:10.5px}
.topbar span{position:absolute;top:13px}
.topbar .divider{position:absolute;left:196px;top:10px;width:1px;height:18px;background:#444}
.topbar svg{position:absolute}
.header{position:absolute;left:0;top:37px;width:1200px;height:80px;background:var(--page)}
.brand{position:absolute;left:162px;top:26px;display:flex;align-items:center;gap:6px;font-size:13px;font-weight:700;color:var(--ink)}
.brand i{width:12px;height:12px;border-radius:50%;background:var(--green);display:block}
.search{position:absolute;left:279px;top:22px;width:539px;height:27px;background:#fff;display:flex;align-items:center;padding-left:10px;gap:10px;font-size:10px;color:var(--muted)}
.category{position:absolute;left:822px;top:22px;width:136px;height:27px;border:1px solid var(--black);background:#fff;font-size:10px;padding:7px 9px;color:var(--black)}
.category svg{position:absolute;right:8px;top:11px}
.search-btn{position:absolute;left:962px;top:22px;width:58px;height:27px;background:var(--black);color:#fff;font-size:10px;border-radius:2px;display:flex;align-items:center;justify-content:center}
.player{position:absolute;left:165px;top:118px;width:637px;height:410px;background:linear-gradient(135deg,#5a5c5a 0%,#7b7f7c 40%,#5e6259 70%,#3f3f3c 100%);border:1px solid #cfcfcf}
.play{position:absolute;left:288px;top:171px;width:69px;height:69px;border-radius:50%;background:var(--green);display:flex;align-items:center;justify-content:center}
.lessons{position:absolute;left:821px;top:118px;width:200px;background:#fff;border:1px solid var(--line);list-style:none}
.lessons li{height:38.3px;border-bottom:1px solid var(--line);font-size:9.5px;color:var(--ink);padding:0 11px;display:flex;align-items:center;justify-content:space-between}
.lessons li:last-child{border-bottom:none}
.lessons li.active{background:var(--green);color:#fff}
.lesson-title{position:absolute;left:165px;top:545px;font-size:15px;font-weight:700;color:var(--black)}
.instructor{position:absolute;left:165px;top:578px;width:637px;height:210px;background:#fff;box-shadow:0 0 4px rgba(0,0,0,.08)}
.avatar{position:absolute;left:19px;top:16px;width:30px;height:30px;border-radius:50%;background:linear-gradient(135deg,#6d7478,#3a4044)}
.name{position:absolute;left:57px;top:15px;font-size:13.3px;color:var(--black)}
.role{position:absolute;left:57px;top:34px;font-size:9.5px;color:var(--ink)}
.chat-btn{position:absolute;left:499px;top:19px;width:96px;height:24px;border-radius:12px;background:var(--green);color:#fff;font-size:11px;display:flex;align-items:center;justify-content:center;gap:6px}
.bio{position:absolute;left:19px;top:65px;width:600px;font-size:11px;line-height:15px;color:var(--text)}
.bio p+p{margin-top:15px}
</style>
</head>
<body>
<div class="topbar">
  <span style="left:158px">Sign in</span>
  <div class="divider"></div>
  <span style="left:205px">Register</span>
  <svg style="left:279px;top:14px" width="8" height="9" viewBox="0 0 24 24"><path fill="#fff" d="M6.6 10.8a15 15 0 0 0 6.6 6.6l2.2-2.2a1 1 0 0 1 1-.25 11.4 11.4 0 0 0 3.6.57 1 1 0 0 1 1 1V20a1 1 0 0 1-1 1A17 17 0 0 1 3 4a1 1 0 0 1 1-1h3.5a1 1 0 0 1 1 1c0 1.25.2 2.45.57 3.6a1 1 0 0 1-.25 1z"/></svg>
  <span style="left:291px">Help &amp; Contact</span>
  <span style="left:884px">Become a Teacher</span>
  <svg style="left:1008px;top:13px" width="10" height="11" viewBox="0 0 24 24"><path fill="#fff" d="M12 22a2.5 2.5 0 0 0 2.5-2.5h-5A2.5 2.5 0 0 0 12 22zm7-6V11a7 7 0 0 0-5.5-6.8V3a1.5 1.5 0 0 0-3 0v1.2A7 7 0 0 0 5 11v5l-2 2v1h18v-1z"/></svg>
</div>

<div class="header">
  <div class="brand"><i></i>LearnHarbor</div>
  <div class="search">
    <svg width="10" height="10" viewBox="0 0 24 24"><circle cx="10" cy="10" r="6.5" fill="none" stroke="#777" stroke-width="2.5"/><path d="M15 15l6 6" stroke="#777" stroke-width="2.5"/></svg>
    Search Courses
  </div>
  <div class="category">All Categories
    <svg width="8" height="5" viewBox="0 0 8 5"><path d="M0 0h8L4 5z" fill="#111"/></svg>
  </div>
  <div class="search-btn">Search</div>
</div>

<div class="player" role="img" aria-label="Lesson video still: modern lounge with armchair and sofa by a city-view window">
  <div class="play">
    <svg width="24" height="26" viewBox="0 0 24 26"><path d="M3 1l20 12L3 25z" fill="#fff"/></svg>
  </div>
</div>

<ul class="lessons">
  <li class="active">Lession1: Lessons Name
    <svg width="6" height="8" viewBox="0 0 6 8"><rect x="0" y="2" width="1" height="4" fill="#fff"/><rect x="2.5" y="0" width="1" height="8" fill="#fff"/><rect x="5" y="2" width="1" height="4" fill="#fff"/></svg>
  </li>
  <li>Lession2: Lessons Name</li>
  <li>Lession3: A long Lessons Name here...</li>
  <li>Lession4: Lessons Name</li>
  <li>Lession5: A long Lessons Name here...</li>
  <li>Lession6: A long Lessons Name here...</li>
  <li>Lession7: Lessons Name</li>
  <li>Lession8: A long Lessons Name here...</li>
  <li>Lession9: Lessons Name</li>
  <li>Lession10: A long Lessons Name here...</li>
  <li>Lession11: A long Lessons Name here...</li>
  <li>Lession11: A long Lessons Name here...</li>
  <li>Lession11: A long Lessons Name here...</li>
</ul>

<h1 class="lesson-title">Lession1: Lessons Name</h1>

<section class="instructor">
  <div class="avatar" role="img" aria-label="Instructor profile photo"></div>
  <div class="name">Instructor’s Name</div>
  <div class="role">Titles of instrutor</div>
  <div class="chat-btn">
    <svg width="14" height="13" viewBox="0 0 24 22"><path d="M12 2C6.5 2 2 5.8 2 10.5c0 2.3 1.1 4.4 2.9 5.9L3.5 21l5-2.6c1.1.3 2.3.6 3.5.6 5.5 0 10-3.8 10-8.5S17.5 2 12 2z" fill="#fff"/></svg>
    Live Chat
  </div>
  <div class="bio">
    <p>A short description of lecturer here Lorem ipsum dolor sit amet, consectetur adipiscing elit, sed do eiusmod tempor incididunt ut labore et dolore magna aliqua. Ut enim ad minim veniam, quis nostrud exercitation.</p>
    <p>Sed ut perspiciatis unde omnis iste natus error sit voluptatem accusantium doloremque laudantium, totam rem aperiam, eaque ipsa quae ab illo inventore veritatis et quasi architecto beatae vitae dicta sunt explicabo. Nemo enim ipsam voluptatem quia voluptas sit aspernatur aut odit aut fugit, sed quia consequuntur magni dolores eos qui ratione voluptatem sequi nesciunt. Neque porro quisquam est, qui dolorem ipsum quia dolor sit amet, consectetur, adipisci velit, sed quia non numquam eius modi tempora incidunt ut labore et dolore magnam aliquam quaerat vol</p>
  </div>
</section>
</body>
</html>
```